Harbor Fresh Cleaning car wrap

I need a car wrap design for my work van that is eye catching and stands out. My type of business is carpet cleaning and tile and grout cleaning along with other services. I would like the services to be listed on the wrap along with the phone number and website.
Also please add that we service Commercial and Residential.
Website is:
HarborFreshCleaning.com
Phone number (555) 203-4619
The services I provide are as follow:
Tile & Grout Cleaning
Carpet Cleaning
Hardwood Floor Cleaning and Refinishing
Upholstery and Rug Cleaning
My business colors consist of blue and white but I am open to using other colors.
My logo is attached in the files.
Commercial and Residential
Carpet Cleaning

```html
<!DOCTYPE html>
<html lang="en">
<head>
<meta charset="utf-8">
<title>Harbor Fresh Cleaning – Van Wrap</title>
<link href="https://fonts.googleapis.com/css2?family=Montserrat:wght@500;600;700;800&display=swap" rel="stylesheet">
<style>
  :root{
    --bg:#1c1c1e;
    --white:#f7f8fa;
    --blue:#0d5aa6;
    --navy:#0a3f7e;
    --teal:#13939a;
    --teal-dark:#0e7b84;
    --charcoal:#2b2d31;
    --tyre:#1a1b1d;
    --rim:#9ea3a8;
    --glass:#3d4045;
    --red:#c62828;
    --ink:#2a2c30;
  }
  html,body{margin:0;padding:0;width:1200px;height:800px;overflow:hidden;background:var(--bg);}
  .wrap-sheet{display:block;width:1200px;height:800px;font-family:"Montserrat",sans-serif;}
  .brand{font-weight:800;fill:var(--teal);}
  .service{font-weight:600;fill:var(--white);}
  .service-dark{font-weight:600;fill:var(--ink);}
  .phone{font-weight:700;fill:var(--white);}
  .site{font-weight:600;fill:var(--white);}
  .site-teal{font-weight:600;fill:#2fb7bd;}
  .tagline{font-weight:600;fill:var(--white);letter-spacing:3px;}
  .icon{fill:none;stroke:var(--white);stroke-width:1.6;}
  .icon-dark{fill:none;stroke:var(--ink);stroke-width:1.4;}
  .divider{stroke:rgba(255,255,255,.45);stroke-width:1;}
  .divider-dark{stroke:rgba(0,0,0,.25);stroke-width:1;}
</style>
</head>
<body>
<svg class="wrap-sheet" viewBox="0 0 1200 800" xmlns="http://www.w3.org/2000/svg">
  <g class="van-side">
    <path class="body" fill="var(--white)" d="M42 300 L50 245 Q58 218 100 206 L180 180 L305 58 Q330 28 370 26 L1120 26 Q1140 28 1142 60 L1146 290 L1150 345 L42 345 Z"/>
    <path class="rear-panel" fill="var(--blue)" d="M862 26 L1120 26 Q1140 28 1142 60 L1146 290 L1150 300 L300 290 C520 275 760 230 862 26 Z"/>
    <path class="swoosh-blue" fill="var(--blue)" d="M112 262 C200 205 330 205 450 240 C560 268 650 270 760 266 L700 285 C560 290 420 250 330 238 C240 228 170 250 128 282 Z"/>
    <path class="swoosh-teal" fill="var(--teal)" d="M145 282 C220 240 320 228 420 250 C330 245 240 260 190 290 Z"/>
    <path class="swoosh-navy" fill="var(--navy)" d="M250 282 C360 240 470 255 560 275 L420 285 Z"/>
    <path class="window" fill="var(--glass)" d="M228 188 L320 80 Q330 60 360 58 L400 58 Q410 60 408 75 L402 180 Q400 190 390 190 Z"/>
    <rect x="262" y="127" width="30" height="58" rx="6" fill="var(--charcoal)"/>
    <rect x="378" y="203" width="32" height="6" rx="3" fill="var(--charcoal)"/>
    <path class="headlight" fill="var(--charcoal)" d="M55 232 L130 220 L118 255 L60 262 Z"/>
    <path class="rocker" fill="var(--charcoal)" d="M40 262 L60 262 L128 282 L140 277 L1146 277 L1160 300 L1160 330 L1120 340 L1010 362 L40 362 Z"/>
    <path class="band-teal" fill="var(--teal)" d="M440 322 L810 322 L790 342 L440 342 Z"/>
    <path class="band-teal-dark" fill="var(--teal-dark)" d="M320 364 C360 340 420 336 470 340 L860 340 L850 364 Z"/>
    <path fill="var(--teal)" d="M335 364 C380 345 430 335 470 334 L465 342 C430 345 390 352 355 364 Z"/>
    <rect x="1124" y="147" width="20" height="130" rx="6" fill="var(--red)"/>
    <g class="wheel"><circle cx="212" cy="350" r="64" fill="var(--tyre)"/><circle cx="212" cy="350" r="40" fill="var(--rim)"/><circle cx="212" cy="350" r="12" fill="var(--charcoal)"/></g>
    <g class="wheel"><circle cx="934" cy="350" r="64" fill="var(--tyre)"/><circle cx="934" cy="350" r="40" fill="var(--rim)"/><circle cx="934" cy="350" r="12" fill="var(--charcoal)"/></g>

    <g class="logo-lockup">
      <text class="brand" x="630" y="128" font-size="40" text-anchor="middle">HARBOR FRESH</text>
      <text class="brand" x="630" y="172" font-size="36" text-anchor="middle">CLEANING</text>
    </g>

    <g class="service-list">
      <g class="icon"><rect x="869" y="67" width="44" height="40"/><path d="M891 67 V107 M869 87 H913"/><circle cx="899" cy="88" r="4"/></g>
      <text class="service" x="926" y="85" font-size="14">TILE &amp; GROUT</text>
      <text class="service" x="926" y="102" font-size="14">CLEANING</text>
      <line class="divider" x1="900" y1="118" x2="1042" y2="118"/>
      <g class="icon"><rect x="848" y="127" width="50" height="34"/><path d="M850 164 H896"/></g>
      <text class="service" x="920" y="143" font-size="14">CARPET</text>
      <text class="service" x="920" y="160" font-size="14">CLEANING</text>
      <line class="divider" x1="880" y1="174" x2="1058" y2="174"/>
      <g class="icon"><rect x="836" y="186" width="52" height="33"/><path d="M842 219 L866 186 M854 219 L878 186 M866 219 L888 191 M836 205 L850 186"/></g>
      <text class="service" x="908" y="200" font-size="14">HARDWOOD FLOOR</text>
      <text class="service" x="908" y="217" font-size="14">CLEANING &amp; REFINISHING</text>
      <line class="divider" x1="870" y1="229" x2="1075" y2="229"/>
      <g class="icon"><path d="M834 262 V245 Q834 240 840 240 H872 Q878 240 878 245 V262 Z M830 250 H838 V262 M882 250 H874 V262 M836 262 V268 M876 262 V268"/></g>
      <text class="service" x="901" y="251" font-size="14">UPHOLSTERY &amp;</text>
      <text class="service" x="901" y="268" font-size="14">RUG CLEANING</text>
    </g>

    <line x1="470" y1="301" x2="500" y2="301" stroke="var(--teal)" stroke-width="2"/>
    <line x1="762" y1="301" x2="792" y2="301" stroke="var(--teal)" stroke-width="2"/>
    <text class="phone" x="631" y="312" font-size="29" text-anchor="middle">(555) 203-4619</text>
    <text class="site" x="628" y="337" font-size="17" text-anchor="middle">HarborFreshCleaning.com</text>
    <text class="tagline" x="632" y="359" font-size="10.5" text-anchor="middle">COMMERCIAL &amp; RESIDENTIAL SERVICES</text>
  </g>

  <g class="van-rear">
    <rect x="324" y="714" width="543" height="68" rx="8" fill="var(--charcoal)"/>
    <path class="body" fill="var(--white)" d="M340 440 Q345 418 370 416 L820 416 Q845 418 850 440 L862 714 L330 714 Z"/>
    <path class="band-blue" fill="var(--blue)" d="M330 558 C420 548 520 585 604 612 C700 638 790 630 858 620 L862 714 L330 714 Z"/>
    <path class="band-navy" fill="var(--navy)" d="M330 652 C450 618 560 655 660 666 C740 674 800 660 860 646 L862 714 L330 714 Z"/>
    <path class="wave-line" fill="var(--white)" d="M604 640 C690 664 780 654 858 648 L858 657 C780 664 690 672 604 648 Z"/>
    <path class="band-teal" fill="var(--teal)" d="M356 690 L720 690 L705 713 L356 713 Z"/>
    <line x1="604" y1="416" x2="604" y2="782" stroke="var(--charcoal)" stroke-width="1.2"/>
    <rect x="328" y="535" width="26" height="155" rx="8" fill="var(--red)"/>
    <rect x="838" y="535" width="26" height="155" rx="8" fill="var(--red)"/>
    <rect x="370" y="758" width="26" height="10" rx="2" fill="var(--red)"/>
    <rect x="795" y="758" width="26" height="10" rx="2" fill="var(--red)"/>

    <g class="logo-lockup">
      <text class="brand" x="498" y="500" font-size="26" text-anchor="middle">HARBOR FRESH</text>
      <text class="brand" x="498" y="530" font-size="23" text-anchor="middle">CLEANING</text>
    </g>

    <g class="service-list">
      <g class="icon-dark"><rect x="640" y="450" width="33" height="31"/><path d="M656 450 V481 M640 465 H673"/></g>
      <text class="service-dark" x="687" y="464" font-size="11">TILE &amp; GROUT</text>
      <text class="service-dark" x="687" y="477" font-size="11">CLEANING</text>
      <line class="divider-dark" x1="670" y1="489" x2="775" y2="489"/>
      <g class="icon-dark"><rect x="633" y="498" width="40" height="27"/></g>
      <text class="service-dark" x="687" y="510" font-size="11">CARPET</text>
      <text class="service-dark" x="687" y="523" font-size="11">CLEANING</text>
      <line class="divider-dark" x1="670" y1="533" x2="775" y2="533"/>
      <g class="icon-dark"><rect x="625" y="543" width="41" height="26"/><path d="M630 569 L650 543 M640 569 L660 543 M650 569 L666 549"/></g>
      <text class="service-dark" x="680" y="554" font-size="11">HARDWOOD FLOOR</text>
      <text class="service-dark" x="680" y="567" font-size="11">CLEANING &amp; REFINISHING</text>
      <line class="divider-dark" x1="670" y1="577" x2="790" y2="577"/>
      <g class="icon-dark"><path d="M625 602 V590 Q625 586 630 586 H654 Q659 586 659 590 V602 Z M621 593 H627 V602 M663 593 H657 V602"/></g>
      <text class="service-dark" x="680" y="592" font-size="11">UPHOLSTERY &amp;</text>
      <text class="service-dark" x="680" y="605" font-size="11">RUG CLEANING</text>
    </g>

    <text class="phone" x="388" y="660" font-size="24">(555) 203-4619</text>
    <text class="site-teal" x="390" y="681" font-size="13.5">HarborFreshCleaning.com</text>
    <text class="tagline" x="393" y="706" font-size="9.5">COMMERCIAL &amp; RESIDENTIAL SERVICES</text>
  </g>
</svg>
</body>
</html>
```